New Body Mist 250 ml exclusive

We are excited to embark on a new project to design the packaging for body mist:
Amber Drizzle

We are looking for a design that is truly unique and stands out, with a touch of individuality that sets it apart. The design should be eye-catching and visually appealing, drawing attention even from a distance. We want the body mists to have a fun and attractive look that appeals to customers.

To help bring your design to life, we will provide the dimensions of the bottle, which has a capacity of 250ml. The bottle measures 13.3 cm in height and 4.9 cm in diameter (excluding the pump). Additionally, we will also provide the dimensions of the label, which measures 15.1 cm in height and 12.8 cm in width.

We believe that giving you the freedom to put your own unique touch and color choices will help create a truly standout design. We look forward to seeing your creative vision for our body mist.

We shared with you the logo of the body mist and some examples of models that we liked.

Please be informed that the project only includes one design and the remaining three will be completed and paid for through a 1on1 project with the winner of the contest.

Target Market(s)

Supermarket and perfumery stores

Industry/Entity Type

Cosmetics

Font styles to use
Serif

Requirements
Must have
• Uniqueness and attractiveness

```html
<!DOCTYPE html>
<html lang="en">
<head>
<meta charset="utf-8">
<title>Amber Drizzle – Body Mist Label</title>
<link rel="stylesheet" href="https://fonts.googleapis.com/css2?family=Josefin+Sans:wght@400;600&family=Montserrat:wght@500&display=swap">
<style>
  :root {
    --backdrop: #1a6df5;
    --label-blue: #2f78c4;
    --label-teal: #4a8fc0;
    --label-violet: #8a6fc0;
    --label-pink: #c58ad0;
    --band-light: rgba(255, 255, 255, 0.72);
    --band-fade: rgba(255, 255, 255, 0.35);
    --title-purple: #8b2c96;
    --caption-grey: #4c4c5c;
    --edge-white: rgba(255, 255, 255, 0.85);
  }
  * { margin: 0; padding: 0; box-sizing: border-box; }
  html, body {
    width: 1200px;
    height: 1200px;
    overflow: hidden;
    background: var(--backdrop);
  }
  .canvas {
    position: relative;
    width: 1200px;
    height: 1200px;
  }
  .label {
    position: absolute;
    left: 210px;
    top: 140px;
    width: 780px;
    height: 920px;
    overflow: hidden;
    background: linear-gradient(170deg, var(--label-blue) 0%, var(--label-teal) 35%, var(--label-violet) 70%, var(--label-pink) 100%);
  }
  .pattern-area {
    position: absolute;
    right: 0;
    bottom: 0;
    width: 520px;
    height: 560px;
    background: radial-gradient(ellipse at 60% 75%, rgba(224, 150, 220, 0.75) 0%, rgba(190, 130, 210, 0.4) 45%, rgba(160, 120, 200, 0) 75%);
  }
  .light-band {
    position: absolute;
    left: 150px;
    top: 0;
    width: 300px;
    height: 100%;
    background: linear-gradient(180deg, var(--band-light) 0%, var(--band-light) 55%, var(--band-fade) 100%);
  }
  .band-edge {
    position: absolute;
    top: 0;
    width: 3px;
    height: 100%;
    background: var(--edge-white);
    opacity: 0.5;
  }
  .band-edge--left { left: 150px; }
  .band-edge--right { left: 447px; }
  .vertical {
    position: absolute;
    writing-mode: vertical-rl;
    transform: rotate(180deg);
    white-space: nowrap;
  }
  .tagline {
    left: 118px;
    bottom: 40px;
    font-family: "Montserrat", sans-serif;
    font-weight: 500;
    font-size: 17px;
    letter-spacing: 0.28em;
    color: var(--edge-white);
  }
  .brand-name {
    left: 196px;
    bottom: 40px;
    font-family: "Josefin Sans", sans-serif;
    font-weight: 600;
    font-size: 96px;
    letter-spacing: 0.04em;
    line-height: 1;
    color: var(--title-purple);
  }
  .product-type {
    left: 310px;
    bottom: 42px;
    font-family: "Montserrat", sans-serif;
    font-weight: 500;
    font-size: 28px;
    letter-spacing: 0.42em;
    color: var(--caption-grey);
  }
</style>
</head>
<body>
  <main class="canvas">
    <section class="label">
      <div class="pattern-area" role="img" aria-label="Decorative pink floral mandala pattern"></div>
      <div class="light-band"></div>
      <div class="band-edge band-edge--left"></div>
      <div class="band-edge band-edge--right"></div>
      <p class="vertical tagline">BODY FRAGRANCE | ORIGINAL FORMULA</p>
      <h1 class="vertical brand-name">AMBER DRIZZLE</h1>
      <p class="vertical product-type">BODY MIST FOR MEN</p>
    </section>
  </main>
</body>
</html>
```